Business Card Design Project : Tidewell Press

In preparation for market launch, Whistler's Tidewell Press require the development of a business card. Tidewell Press is a Community online publishing web portal. We provide the the city of Whistler located in B.C. (Canada) business directories, News, Classified ads, News, Events and blogs etc.

The main focus of the brand is to help local businesses to corporate with their online advertisement and marketing. Meeting our clients face to face is a must (B2B).

Target Market(s)

The target market is B2B customers. Business Owners to Marketing, advertising Managers

Industry/Entity Type

Business

Requirements
Must have
• - The business card will be two sided.
the BACK side will have our logo which consist of (icon, url,slogan) submited. The logo will be middle and centred.

The FRONT side should have company details:

Company Legal Name: FERNDALE TIDEWELL PRESS

Owen Marsk
Director of Sales & Marketing

www.ferndaletidewell.biz
owen@ferndaletidewell.biz

Phone: 555 014 3826
#2817 - 562 E. Harlow Ave.
Vancouver, B.C. K7P2R4 Canada
Nice to have
• - For the "FRONT" side of our business card. You can separate or re-arrange with our logo components (icon, logo,slogan). It does not have to be together.

Also our company legal name is rather long so arrange or organize the name in a way to make it shorter. Your experience and creativity will have to come in play.
Should not have
• should not have other colors beside logo color and black text (2 colors). Also nothing Three dimensional

```html
<!DOCTYPE html>
<html lang="en">
<head>
<meta charset="utf-8">
<title>Tidewell Press – Business Card</title>
<link rel="stylesheet" href="https://fonts.googleapis.com/css2?family=Open+Sans:wght@400;600;700&display=swap">
<style>
  :root {
    --brand-blue: #3a8ff0;
    --ink: #141414;
    --paper: #ffffff;
    --backdrop: #e8eae9;
    --edge: #cfd3d1;
  }
  * { box-sizing: border-box; margin: 0; padding: 0; }
  html, body {
    width: 1200px;
    height: 606px;
    overflow: hidden;
    background: var(--backdrop);
    font-family: "Open Sans", Arial, sans-serif;
    color: var(--ink);
  }
  .stage {
    position: relative;
    width: 1200px;
    height: 606px;
  }
  .card {
    position: absolute;
    top: 148px;
    width: 540px;
    height: 309px;
    background: var(--paper);
    border: 1px solid var(--edge);
  }
  .card--front { left: 40px; }
  .card--back  { left: 620px; }

  /* Front side */
  .front__company {
    position: absolute;
    top: 22px;
    right: 26px;
    text-align: right;
  }
  .front__legal-name {
    font-size: 17px;
    font-weight: 700;
    letter-spacing: 0.3px;
  }
  .front__slogan {
    font-size: 15px;
    color: var(--brand-blue);
    margin-top: 1px;
  }
  .front__wordmark {
    position: absolute;
    top: 82px;
    left: 26px;
    display: flex;
    align-items: center;
    gap: 10px;
  }
  .wordmark__dot {
    width: 16px;
    height: 16px;
    border-radius: 50%;
    background: var(--brand-blue);
  }
  .wordmark__text {
    font-weight: 700;
    color: var(--brand-blue);
  }
  .front__wordmark .wordmark__text { font-size: 30px; }
  .front__person {
    position: absolute;
    top: 112px;
    left: 240px;
    width: 250px;
    text-align: center;
  }
  .person__name { font-size: 19px; }
  .person__title { font-size: 13px; margin-top: 1px; }
  .front__rule {
    position: absolute;
    top: 176px;
    left: 26px;
    right: 26px;
    height: 1.5px;
    background: var(--brand-blue);
  }
  .front__contact {
    position: absolute;
    left: 26px;
    top: 196px;
    font-size: 14px;
    line-height: 1.45;
  }
  .front__online {
    position: absolute;
    right: 26px;
    top: 196px;
    font-size: 14px;
    line-height: 1.45;
    text-align: right;
  }

  /* Back side */
  .back__url {
    position: absolute;
    top: 34px;
    left: 0;
    right: 0;
    text-align: center;
    font-size: 27px;
    font-weight: 700;
  }
  .back__wordmark {
    position: absolute;
    top: 112px;
    left: 0;
    right: 0;
    display: flex;
    justify-content: center;
    align-items: center;
    gap: 14px;
  }
  .back__wordmark .wordmark__dot { width: 26px; height: 26px; }
  .back__wordmark .wordmark__text { font-size: 52px; }
  .back__slogan {
    position: absolute;
    bottom: 34px;
    left: 0;
    right: 0;
    text-align: center;
    font-size: 25px;
  }
</style>
</head>
<body>
<main class="stage">

  <section class="card card--front" aria-label="Business card front">
    <div class="front__company">
      <p class="front__legal-name">FERNDALE TIDEWELL PRESS</p>
      <p class="front__slogan">Your information gateway</p>
    </div>

    <div class="front__wordmark">
      <span class="wordmark__dot"></span>
      <span class="wordmark__text">Tidewell Press</span>
    </div>

    <div class="front__person">
      <p class="person__name">Owen Marsk</p>
      <p class="person__title">Director of Sales &amp; Marketing</p>
    </div>

    <div class="front__rule"></div>

    <address class="front__contact" style="font-style: normal;">
      Phone: 555 014 3826<br>
      #2817 - 562 E. Harlow Ave.<br>
      Vancouver, B.C. K7P2R4 Canada
    </address>

    <div class="front__online">
      www.ferndaletidewell.biz<br>
      owen@ferndaletidewell.biz
    </div>
  </section>

  <section class="card card--back" aria-label="Business card back">
    <p class="back__url">www.ferndaletidewell.biz</p>
    <div class="back__wordmark">
      <span class="wordmark__dot"></span>
      <span class="wordmark__text">Tidewell Press</span>
    </div>
    <p class="back__slogan">Your information gateway</p>
  </section>

</main>
</body>
</html>
```